Business Card Design

I require the design of business cards using my exisiting logo.

It is essential that the designer has experience with various print processes (foil stamping etc) and different paper stock.

The design is to blend in with current packaging and display unit. (Images will be provided).
A swing tag and certificate of authenticity design will als be required at a later stage.

Details which need to be included on the card are:
- Contact Name
- Position in Company
- Address
- Contact Number
- Email Address
- Web Address

Ideally I would prefer the background (both sides) to be greyish colour (offset printing or if you can suggest greyish paperstock) with silver foiling on the front and either black or metallic silver on the back.

Or another option would be grey background on the front and either white or black on the the back.

* The business card can be portrait or landscape.

Printers specifications:
Bleed 3mm
Trim Marks
Seperate file for foil printing

This task is for someone who is creative and enjoys working with fashion and luxury items!
_______________________________________________

I will require business cards designs for 2 different business and would hope to work with the same designer.

Please note I had asked for a grey colour at least on one of the sides. However I keep on getting black and white designs.   

Industry/Entity Type

Business

Requirements
Must have
• - Double sided business card
- Luxury feel
- Foil Print Priniting

- Would prefer at least grey background at least on one side of the card.

- The business card can be portrait or landscape.
Nice to have
• *The business card can be portrait or landscape.
Should not have
• - Bright Colours
- Alterations to logo

```html
<!DOCTYPE html>
<html lang="en">
<head>
<meta charset="utf-8">
<title>Business Card – Front and Back</title>
<link rel="stylesheet" href="https://fonts.googleapis.com/css2?family=Open+Sans:wght@300;400;600&display=swap">
<style>
  :root {
    --backdrop: #121212;
    --grey: #7b7b84;
    --grey-dark: #5f5f68;
    --navy: #2f2a6f;
    --paper: #ffffff;
    --silver: #eceef2;
    --ink: #111111;
    --rule: #c9c9d6;
  }
  html, body {
    margin: 0;
    padding: 0;
    width: 1200px;
    height: 849px;
    overflow: hidden;
    background: var(--backdrop);
    font-family: "Open Sans", Arial, sans-serif;
  }
  .canvas {
    position: relative;
    width: 1200px;
    height: 849px;
    display: flex;
    align-items: center;
    justify-content: center;
    gap: 40px;
  }
  .card {
    position: relative;
    width: 540px;
    height: 310px;
    overflow: hidden;
  }

  /* Front: grey stock with silver-foil brand name */
  .card--front {
    background: linear-gradient(135deg, var(--grey) 0%, var(--grey-dark) 100%);
    display: flex;
    align-items: center;
    justify-content: center;
  }
  .brand {
    display: flex;
    align-items: center;
    gap: 18px;
  }
  .brand__name {
    font-weight: 300;
    letter-spacing: 0.04em;
    color: var(--silver);
    white-space: nowrap;
  }
  .brand__dot {
    display: block;
    border-radius: 50%;
    background: var(--silver);
  }
  .card--front .brand__name { font-size: 52px; }
  .card--front .brand__dot { width: 46px; height: 46px; }

  /* Back: contact details with navy band */
  .card--back { background: var(--paper); }
  .contact {
    position: absolute;
    left: 38px;
    top: 30px;
    color: var(--ink);
  }
  .contact__name {
    margin: 0;
    font-size: 26px;
    font-weight: 400;
    line-height: 1.1;
    color: var(--navy);
  }
  .contact__role {
    margin: 0;
    font-size: 13px;
    line-height: 1.2;
  }
  .contact__details {
    list-style: none;
    margin: 0;
    padding: 0;
    position: absolute;
    left: 78px;
    top: 124px;
    font-size: 22px;
    line-height: 1.15;
    color: var(--ink);
  }
  .contact__details li:last-child { margin-top: 10px; }

  .band {
    position: absolute;
    top: 0;
    bottom: 0;
    left: 352px;
    width: 142px;
    background: var(--navy);
  }
  .band__label {
    position: absolute;
    top: 20px;
    left: -6px;
    width: 154px;
    height: 80px;
    background: var(--paper);
    border: 1px solid var(--rule);
    box-sizing: border-box;
    display: flex;
    align-items: center;
    justify-content: center;
  }
  .band__label .brand { gap: 8px; }
  .band__label .brand__name { font-size: 20px; color: var(--navy); }
  .band__label .brand__dot { width: 14px; height: 14px; background: var(--navy); }
</style>
</head>
<body>
  <main class="canvas">
    <section class="card card--front" aria-label="Card front">
      <div class="brand">
        <span class="brand__name">ORA GEMS</span>
        <span class="brand__dot" aria-hidden="true"></span>
      </div>
    </section>

    <section class="card card--back" aria-label="Card back">
      <div class="contact">
        <h1 class="contact__name">Contact Name</h1>
        <p class="contact__role">Position in Company</p>
      </div>
      <ul class="contact__details">
        <li>Address</li>
        <li>Contact Number</li>
        <li>Email Address</li>
        <li>Web Address</li>
      </ul>
      <div class="band">
        <div class="band__label">
          <div class="brand">
            <span class="brand__name">ORA GEMS</span>
            <span class="brand__dot" aria-hidden="true"></span>
          </div>
        </div>
      </div>
    </section>
  </main>
</body>
</html>
```